Federal IT Consulting Company - Corvalen Advisory Partners

We're seeking a skilled web designer to create a modern, bold, and engaging WordPress website for Corvalen Advisory Partners, LLC. Our company specializes in federal IT consulting, and our name is a play on "Charting Circuitry." The website should reflect our expertise in the federal technology marketplace and position us as a trusted partner for clients navigating their IT journey.

contact: info@corvalenadv.example

Current Status

WordPress is already installed on our hosting account
We have an existing logo (may need modernization)

Design Requirements

Style:

Modern and visually striking design
Bold elements to convey confidence and expertise
Incorporate the concept of "charting circuitry" into the design

Features:

Modern UX sliders for dynamic content presentation
Eye-catching, high-quality images (stock photos to be sourced by the designer)
Responsive design for all devices

Color Scheme:

To be proposed by the designer, should align with our brand and convey trust and technological expertise

Logo:

Evaluate our current logo
Create a transparent background version if needed
Propose modernization if deemed necessary

Accessibility:

Ensure design elements are accessible to users with disabilities
Use high contrast ratios for text and background colors
Provide text alternatives for non-text content

Website Structure
Create the following pages, with the possibility of subpages:

Home
Services
About
Contact

Specific Page Requirements
Home Page

Striking hero section with a clear value proposition
Overview of our services
Client testimonials or trust indicators

Services Page

Detailed list of our IT consulting services
Clear explanation of how we help navigate the federal IT landscape

About Page

Company history and mission
Team highlights (if applicable)
Our approach to federal IT consulting

Contact Page

Contact form
Other contact methods (phone, email)

Technical Requirements

Fully responsive design
SEO best practices implemented
Fast loading times
Integration with necessary plugins (to be discussed)
Training on how to update and maintain the site
Full compliance with Web Content Accessibility Guidelines (WCAG) 2.1 Level AA
Adherence to Section 508 standards for federal website accessibility
Implementation of necessary features for ADA compliance

Target Market(s)

US Federal Govt customers looking for IT support.

Industry/Entity Type

IT Consulting

Coding

Coded - Design and coding required

Colors
0054AA
0677BA
7BADD7
CADEEF
E8F1F8
0094D4
00A9DD
6FCCEA
C7EBF8
E9F6FB
00AB8E
00BBA5
67D7C9
C6EFE9
E9F9F6

```html
<!DOCTYPE html>
<html lang="en">
<head>
<meta charset="utf-8">
<title>Corvalen Federal Services</title>
<link rel="stylesheet" href="https://fonts.googleapis.com/css2?family=Montserrat:wght@300;400;500;600;700&family=Tinos&display=swap">
<style>
:root{
  --blue:#0054AA;
  --blue-dark:#00478f;
  --blue-mid:#0677BA;
  --sky:#00A9DD;
  --sky-soft:#C7EBF8;
  --green:#00AB8E;
  --green-light:#67D7C9;
  --ink:#1d1d1f;
  --text:#5a5a5a;
  --line:#d9dde3;
  --white:#ffffff;
  --star:#f5a623;
}
*{margin:0;padding:0;box-sizing:border-box}
html,body{width:1200px;height:4702px;overflow:hidden}
body{position:relative;background:var(--white);font-family:"Montserrat",sans-serif;color:var(--ink)}
.abs{position:absolute}
.serif{font-family:"Tinos",serif}

/* header */
.site-header{position:absolute;left:0;top:0;width:1200px;height:72px;background:var(--white);z-index:5}
.brand{position:absolute;left:112px;top:18px;display:flex;align-items:center;gap:10px}
.brand-dot{width:34px;height:34px;border-radius:50%;background:var(--sky)}
.brand-name{font-weight:700;font-size:30px;letter-spacing:1px;color:var(--blue)}
.main-nav{position:absolute;left:370px;top:30px;display:flex;gap:24px;font-size:13px;color:#333}
.main-nav .active{color:var(--green)}
.lang{position:absolute;left:740px;top:24px;display:flex;align-items:center;gap:8px;font-size:12px;color:#444}
.lang-flag{width:30px;height:30px;border-radius:50%;background:linear-gradient(#c8102e 0 40%,#fff 40% 60%,#012169 60%)}
.header-cta{position:absolute;right:0;top:0;width:380px;height:72px}
.header-cta svg{position:absolute;left:0;top:0}
.cta-text{position:absolute;left:120px;top:16px;color:var(--white)}
.cta-text small{display:block;font-size:12.5px}
.cta-text strong{display:block;font-size:21px;font-weight:700;margin-top:1px}
.cta-phone{position:absolute;left:70px;top:22px}

/* hero */
.hero{position:absolute;left:0;top:72px;width:1200px;height:623px;background:var(--blue);border-radius:0 0 240px 240px;overflow:hidden}
.hero-photo{position:absolute;left:520px;top:0;width:680px;height:623px;clip-path:polygon(42% 0,100% 0,100% 100%,0 100%);background:linear-gradient(135deg,#e9edf1 0%,#b9c1c9 45%,#6c7480 80%,#3f4651 100%)}
.hero-copy{position:absolute;left:142px;top:170px;color:var(--white);text-align:center;width:430px}
.hero-title{font-size:86px;font-weight:700;letter-spacing:2px;line-height:1}
.hero-sub{font-size:44px;font-weight:400;letter-spacing:1px;margin-top:6px}
.btn{display:inline-flex;align-items:center;justify-content:center;background:var(--green);color:var(--white);font-weight:700;font-size:13px;letter-spacing:.3px;text-transform:uppercase}
.hero-btn{margin-top:18px;width:298px;height:38px}
.hero-dots{position:absolute;left:330px;top:562px;display:flex;gap:7px}
.hero-dots span{width:9px;height:9px;border-radius:50%;background:rgba(255,255,255,.45)}
.hero-dots span:first-child{background:var(--white)}

/* about */
.about-visual{position:absolute;left:200px;top:850px;width:276px;height:276px;border-radius:50%;background:linear-gradient(160deg,#d8dfe6,#8e98a3);border:14px solid var(--sky-soft)}
.about-copy{position:absolute;left:620px;top:780px;width:470px}
.section-title{font-weight:600;font-size:42px;letter-spacing:.5px}
.rule{width:80px;height:2px;background:var(--green);margin-top:14px}
.about-lead{color:var(--green);font-size:14px;margin-top:20px}
.about-copy p.body{font-size:11.5px;line-height:21px;color:var(--text);text-align:justify;margin-top:10px;font-weight:300}
.about-copy p.body + p.body{margin-top:22px}
.btn-arrow{gap:12px;padding:0 10px 0 24px;height:37px}
.btn-arrow i{display:inline-block;width:18px;height:18px;border:2px solid var(--white);position:relative}
.btn-arrow i::after{content:"";position:absolute;left:4px;top:3px;border-left:6px solid var(--white);border-top:4px solid transparent;border-bottom:4px solid transparent}
.about-btn{margin-top:22px;width:150px}

/* services */
.services{position:absolute;left:0;top:1330px;width:1200px;height:735px;background:var(--blue);border-radius:230px}
.services .section-title{color:var(--white);text-align:center;margin-top:95px}
.services .rule{margin:14px auto 0}
.service-grid{position:absolute;left:124px;top:200px;display:grid;grid-template-columns:461px 461px;gap:28px 30px}
.service-card{height:186px;border:1.5px solid rgba(255,255,255,.45);border-radius:16px;display:flex;gap:30px;padding:36px 24px 0 30px;color:var(--white)}
.service-card.is-featured{background:var(--green);border-color:var(--green)}
.service-card svg{flex:none}
.service-card h3{font-size:20px;font-weight:600}
.service-card p{font-size:12.5px;line-height:26px;margin-top:10px}

/* testimonials */
.testimonials{position:absolute;left:0;top:2150px;width:1200px;text-align:center}
.kicker{font-size:21px;font-weight:300;color:#333}
.testimonials .section-title{margin-top:10px}
.testimonials .rule{margin:14px auto 0}
.review-row{position:absolute;left:112px;top:150px;display:flex;gap:23px;text-align:left}
.review{position:relative;width:227px;height:260px;border:2px solid #3a2f33;padding:18px 20px}
.review-head{display:flex;gap:10px;align-items:center}
.avatar{width:34px;height:34px;border-radius:50%;color:var(--white);font-size:14px;display:flex;align-items:center;justify-content:center}
.review-head b{display:block;font-size:13px;font-weight:600}
.review-head small{font-size:10px;color:#444}
.stars{color:var(--star);font-size:13px;letter-spacing:3px;margin-top:10px}
.review p{font-size:11.5px;line-height:21px;color:#333;margin-top:6px}
.review-badge{position:absolute;right:22px;bottom:16px;width:36px;height:36px;border-radius:50%;background:#e7ebef}
.slide-arrow{position:absolute;top:280px;width:30px;height:30px;border-radius:50%;background:#eceef0;color:#666;font-size:16px;line-height:30px;text-align:center}

/* news */
.news-band{position:absolute;left:0;top:2685px;width:1200px;height:395px;background:var(--green);border-radius:200px 200px 0 0}
.news-band .section-title{color:var(--white);text-align:center;margin-top:75px}
.news-band .rule{margin:14px auto 0;background:var(--white)}
.news-row{position:absolute;left:112px;top:2893px;display:flex;gap:36px}
.news-card{width:301px;height:404px;background:var(--white);border:1px solid var(--line);padding:12px 12px 0}
.news-img{height:184px;background:linear-gradient(135deg,#cfd6dc,#7d8894)}
.news-card h3{font-family:"Tinos",serif;font-weight:400;font-size:22px;line-height:26px;color:#333;margin:22px 0 0 12px}
.news-card p{font-size:12px;line-height:21px;color:var(--text);margin:14px 12px 0;font-weight:300}
.news-card a{display:block;font-size:12px;color:var(--green);text-decoration:underline;margin:18px 0 0 14px}
.news-more{position:absolute;left:527px;top:3322px;width:146px}

/* contact */
.contact{position:absolute;left:0;top:3480px;width:1200px}
.contact .section-title{text-align:center}
.contact .rule{margin:14px auto 0}
.map-field{position:absolute;left:20px;top:95px;width:1160px;height:520px;border-radius:60px;background:radial-gradient(ellipse at center,#f3f5f8 0%,#f8f9fb 60%,#ffffff 100%)}
.contact-form{position:absolute;left:253px;top:112px;width:692px}
.field label{display:block;font-size:12px;color:#555;margin-bottom:8px}
.field .box{border:1px solid var(--line);height:56px;background:var(--white)}
.field-row{display:flex;gap:24px}
.field-row .field{flex:1}
.field + .field, .field-row + .field{margin-top:26px}
.field .box.tall{height:178px}
.submit{position:absolute;left:271px;top:448px;width:148px}

/* footer */
.site-footer{position:absolute;left:0;top:4232px;width:1200px;height:470px;background:var(--blue);border-radius:220px 220px 0 0;color:var(--white)}
.foot-cta{position:absolute;left:162px;top:82px}
.foot-cta small{display:block;font-family:"Tinos",serif;font-size:16px}
.foot-cta strong{display:block;font-size:22px;font-weight:700;margin-top:6px}
.foot-brand{position:absolute;left:460px;top:92px;display:flex;align-items:center;gap:12px}
.foot-brand .brand-dot{width:48px;height:48px;background:var(--white)}
.foot-brand .brand-name{color:var(--white);font-size:40px}
.follow{position:absolute;left:836px;top:108px;display:flex;align-items:center;gap:14px;font-family:"Tinos",serif;font-size:16px}
.follow span{width:14px;height:14px;border-radius:50%;border:1.5px solid var(--white)}
.foot-nav{position:absolute;left:112px;top:182px;width:976px;height:64px;border-top:1px solid rgba(255,255,255,.5);border-bottom:1px solid rgba(255,255,255,.5);display:flex;justify-content:center;align-items:center;gap:24px;font-size:13px}
.foot-info{position:absolute;left:208px;top:280px;display:flex;gap:0}
.info-item{display:flex;gap:18px;width:310px}
.info-icon{width:60px;height:60px;border-radius:50%;background:var(--green);display:flex;align-items:center;justify-content:center;flex:none}
.info-item b{display:block;font-weight:400;font-size:17px;margin-top:6px}
.info-item small{display:block;font-size:11px;line-height:20px;margin-top:4px}
.copyright{position:absolute;left:0;bottom:0;width:1200px;height:42px;background:var(--blue-dark);font-size:12px;text-align:center;line-height:42px}
</style>
</head>
<body>

<header class="site-header">
  <div class="brand"><span class="brand-dot"></span><span class="brand-name">CORVALEN</span></div>
  <nav class="main-nav">
    <span class="active">HOME</span><span>ABOUT US</span><span>SERVICES</span><span>CONTACT</span>
  </nav>
  <div class="lang"><span class="lang-flag"></span>ENG &#8964;</div>
  <div class="header-cta">
    <svg width="380" height="72" viewBox="0 0 380 72">
      <polygon points="30,0 44,0 14,72 0,72" fill="var(--green)"/>
      <polygon points="50,0 380,0 380,72 20,72" fill="var(--blue)"/>
    </svg>
    <svg class="cta-phone" width="30" height="30" viewBox="0 0 24 24" fill="none" stroke="#fff" stroke-width="1.4">
      <path d="M5 3h4l2 5-2.5 1.5a11 11 0 0 0 6 6L16 13l5 2v4a2 2 0 0 1-2 2A16 16 0 0 1 3 5a2 2 0 0 1 2-2z"/>
    </svg>
    <div class="cta-text"><small>Schedule A Free Consultation</small><strong>+1 888 888 8888</strong></div>
  </div>
</header>

<section class="hero">
  <div class="hero-photo" role="img" aria-label="Two consultants in suits reviewing a tablet in a bright office"></div>
  <div class="hero-copy">
    <h1 class="hero-title">CORVALEN</h1>
    <div class="hero-sub">FEDERAL SERVICES</div>
    <span class="btn hero-btn">Schedule my free consultation</span>
  </div>
  <div class="hero-dots"><span></span><span></span><span></span><span></span></div>
</section>

<section>
  <div class="about-visual" role="img" aria-label="Team members talking beside computer monitors in an office"></div>
  <div class="about-copy">
    <h2 class="section-title">ABOUT ME</h2>
    <div class="rule"></div>
    <p class="about-lead serif">Lorem ipsum dolor sit amet, consectetur adipiscing elit, sed do</p>
    <p class="body">Lorem ipsum dolor sit amet, consectetur adipiscing elit, sed do eiusmod tempor incididunt ut labore et dolore magna aliqua. Ut enim ad minim veniam, quis nostrud exercitation ullamco laboris nisi ut aliquip ex ea commodo consequat. Duis aute irure dolor in reprehenderit in voluptate velit esse cillum dolore eu fugiat nulla pariatur.</p>
    <p class="body">Excepteur sint occaecat cupidatat non proident, sunt in culpa qui officia deserunt mollit anim id est laborum. Lorem ipsum dolor sit amet, consectetur adipiscing elit, sed do eiusmod tempor incididunt ut labore et dolore magna aliqua. Ut enim ad minim veniam, quis nostrud exercitation ullamco laboris nisi ut aliquip ex ea commodo consequat. Duis aute irure dolor in reprehenderit in voluptate velit esse cillum dolore eu fugiat nulla pariatur.</p>
    <span class="btn btn-arrow about-btn">Learn more <i></i></span>
  </div>
</section>

<section class="services">
  <h2 class="section-title">OUR SERVICES</h2>
  <div class="rule" style="background:#fff"></div>
  <div class="service-grid">
    <div class="service-card is-featured">
      <svg width="66" height="66" viewBox="0 0 66 66" fill="none" stroke="#fff" stroke-width="2">
        <rect x="30" y="4" width="30" height="18" rx="3"/><path d="M38 22l-4 6 10-6"/>
        <circle cx="18" cy="20" r="6"/><path d="M8 44v-8a10 10 0 0 1 20 0v8"/>
        <path d="M4 48h58M10 48v14M56 48v14"/>
      </svg>
      <div><h3>Lorem ipsum dolor sit</h3><p>They would offer free initial consultations to evaluate potential cases and advise clients on the viability of their claims.</p></div>
    </div>
    <div class="service-card">
      <svg width="66" height="66" viewBox="0 0 66 66" fill="none" stroke="#fff" stroke-width="2">
        <path d="M12 4h32l10 10v48H12z"/><path d="M44 4v10h10"/>
        <circle cx="32" cy="30" r="10"/><path d="M27 42l-3 12 8-4 8 4-3-12"/>
      </svg>
      <div><h3>Lorem ipsum dolor sit</h3><p>Detailed investigation services to gather evidence such as medical reports, photographs, witness statements, and</p></div>
    </div>
    <div class="service-card">
      <svg width="66" height="66" viewBox="0 0 66 66" fill="none" stroke="#fff" stroke-width="2">
        <rect x="14" y="8" width="40" height="52" rx="3"/><rect x="26" y="4" width="16" height="8" rx="2"/>
        <path d="M20 24l3 3 5-6M34 24h14M20 38l3 3 5-6M34 38h14M34 50h14"/>
      </svg>
      <div><h3>Lorem ipsum dolor sit</h3><p>Representation in court or in settlement negotiations to secure compensation for medical expenses, pain and suffering.</p></div>
    </div>
    <div class="service-card">
      <svg width="66" height="66" viewBox="0 0 66 66" fill="none" stroke="#fff" stroke-width="2">
        <path d="M16 4h30l8 8v30H16z"/><circle cx="35" cy="22" r="9"/><path d="M31 22l3 3 5-6"/>
        <path d="M4 50l10-6 12 4 10-2 10 4 14-6M14 58l10 4 14-4"/>
      </svg>
      <div><h3>Lorem ipsum dolor sit</h3><p>Skilled in negotiating with insurance companies, hotel chains, and property owners to obtain fair settlements.</p></div>
    </div>
  </div>
</section>

<section class="testimonials">
  <div class="kicker">What People Say About Us</div>
  <h2 class="section-title">CLIENT TESTIMONIALS</h2>
  <div class="rule"></div>
  <span class="slide-arrow" style="left:40px">&#8249;</span>
  <span class="slide-arrow" style="left:1130px">&#8250;</span>
  <div class="review-row">
    <article class="review">
      <div class="review-head"><span class="avatar" style="background:#f5b400">M</span><div><b>Marla Quinby</b><small>26 July 2023</small></div></div>
      <div class="stars">★★★★★</div>
      <p>Lorem ipsum dolor sit amet, consectetur adipiscing elit, sed do eiusmod tempor incididunt ut labore et dolore magna aliqua.</p>
      <span class="review-badge"></span>
    </article>
    <article class="review">
      <div class="review-head"><span class="avatar" style="background:#34a853">O</span><div><b>Owen Pratt</b><small>17 May 2023</small></div></div>
      <div class="stars">★★★★★</div>
      <p>Lorem ipsum dolor sit amet, consectetur adipiscing elit, sed do eiusmod tempor incididunt ut labore et dolore magna aliqua.</p>
      <span class="review-badge"></span>
    </article>
    <article class="review">
      <div class="review-head"><span class="avatar" style="background:#ea4335">L</span><div><b>Lena Corral</b><small>12 May 2023</small></div></div>
      <div class="stars">★★★★★</div>
      <p>Lorem ipsum dolor sit amet, consectetur adipiscing elit, sed do eiusmod tempor incididunt ut labore et dolore magna aliqua.</p>
      <span class="review-badge"></span>
    </article>
    <article class="review">
      <div class="review-head"><span class="avatar" style="background:#4285f4">R</span><div><b>Reid Halvers</b><small>29 April 2023</small></div></div>
      <div class="stars">★★★★★</div>
      <p>Lorem ipsum dolor sit amet, consectetur adipiscing elit, sed do eiusmod tempor incididunt ut labore et dolore magna aliqua.</p>
      <span class="review-badge"></span>
    </article>
  </div>
</section>

<section>
  <div class="news-band">
    <h2 class="section-title">LATEST NEWS</h2>
    <div class="rule"></div>
  </div>
  <div class="news-row">
    <article class="news-card">
      <div class="news-img" role="img" aria-label="Business people meeting at a desk with laptops"></div>
      <h3>Lorem ipsum dolor<br>sit amet</h3>
      <p>Lorem ipsum dolor sit amet, consec tetur adipiscing elit, sed do eiusmod tempor incididunt</p>
      <a>READ MORE »</a>
    </article>
    <article class="news-card">
      <div class="news-img" role="img" aria-label="Colleagues shaking hands across a meeting table"></div>
      <h3>Lorem ipsum dolor<br>sit amet</h3>
      <p>Lorem ipsum dolor sit amet, consec tetur adipiscing elit, sed do eiusmod tempor incididunt</p>
      <a>READ MORE »</a>
    </article>
    <article class="news-card">
      <div class="news-img" role="img" aria-label="Team gathered around a laptop in a workspace"></div>
      <h3>Lorem ipsum dolor<br>sit amet</h3>
      <p>Lorem ipsum dolor sit amet, consec tetur adipiscing elit, sed do eiusmod tempor incididunt</p>
      <a>READ MORE »</a>
    </article>
  </div>
  <span class="btn btn-arrow news-more">View more <i></i></span>
</section>

<section class="contact">
  <h2 class="section-title">GET IN TOUCH</h2>
  <div class="rule"></div>
  <div class="map-field" role="img" aria-label="Faint dotted world map behind the form"></div>
  <form class="contact-form">
    <div class="field-row">
      <div class="field"><label>Full name</label><div class="box"></div></div>
      <div class="field"><label>Phone</label><div class="box"></div></div>
    </div>
    <div class="field"><label>Email</label><div class="box"></div></div>
    <div class="field"><label>How can we help?</label><div class="box tall"></div></div>
    <span class="btn btn-arrow submit">Submit <i></i></span>
  </form>
</section>

<footer class="site-footer">
  <div class="foot-cta"><small>100% Free Consultation</small><strong>+1 888 888 8888</strong></div>
  <div class="foot-brand"><span class="brand-dot"></span><span class="brand-name">CORVALEN</span></div>
  <div class="follow">Follow us : <span></span><span></span><span></span></div>
  <nav class="foot-nav">
    <span>HOME</span><span>ABOUT US</span><span>SERVICES</span><span>CONTACT</span><span>PRIVACY POLICY</span><span>TERMS OF SERVICES</span>
  </nav>
  <div class="foot-info">
    <div class="info-item">
      <span class="info-icon"><svg width="24" height="24" viewBox="0 0 24 24" fill="#fff"><path d="M12 2a7 7 0 0 0-7 7c0 5 7 13 7 13s7-8 7-13a7 7 0 0 0-7-7zm0 9.5A2.5 2.5 0 1 1 12 6.5a2.5 2.5 0 0 1 0 5z"/></svg></span>
      <div><b>Address :</b><small>123,Lorem ipsum dolor sit<br>amet, consect</small></div>
    </div>
    <div class="info-item">
      <span class="info-icon"><svg width="26" height="26" viewBox="0 0 24 24" fill="#fff"><path d="M3 6h18v12H3z"/><path d="M3 6l9 7 9-7" stroke="#00AB8E" stroke-width="1.6" fill="none"/></svg></span>
      <div><b>Email Address :</b><small>info@corvalenadv.example</small></div>
    </div>
    <div class="info-item">
      <span class="info-icon"><svg width="24" height="24" viewBox="0 0 24 24" fill="#fff"><path d="M5 3h4l2 5-2.5 1.5a11 11 0 0 0 6 6L16 13l5 2v4a2 2 0 0 1-2 2A16 16 0 0 1 3 5a2 2 0 0 1 2-2z"/></svg></span>
      <div><b>Phone :</b><small>+1 888 888 8888</small></div>
    </div>
  </div>
  <div class="copyright">© Copyrights 2024 | All Rights Reserved</div>
</footer>

</body>
</html>
```